Australian Software Consultancy needs new Business Card Design

Design Business Card based on existing design artefacts (attached). We are open to all designs. As its a 2 sided design and we thought it might be quite striking to have one side with a black background and te other side with a white background.

Target Market(s)

Financial Services mainly.

Industry/Entity Type

Business

Contact Information for Business Card

Name :
Position :
Email :

Requirements
Must have
• Funky design using our existing assets

```html
<!DOCTYPE html>
<html lang="en">
<head>
<meta charset="UTF-8">
<title>Field Point — Business Card</title>
<link href="https://fonts.googleapis.com/css2?family=Exo+2:wght@600;700&family=Open+Sans:wght@400;600&display=swap" rel="stylesheet">
<style>
  :root {
    --stage: #808080;
    --paper: #ffffff;
    --ink: #000000;
    --night-top: #1c1c1c;
    --night-bottom: #050505;
    --brand-red: #e31e24;
    --text-light: #ffffff;
    --rule: #6b6b6b;
  }
  * { margin: 0; padding: 0; box-sizing: border-box; }
  html, body {
    width: 1200px; height: 900px; overflow: hidden;
    background: var(--stage);
  }
  .stage { position: relative; width: 1200px; height: 900px; }

  .card {
    position: absolute; top: 184px; height: 490px;
    border-radius: 14px; overflow: hidden;
  }
  .card--front { left: 299px; width: 301px; background: var(--paper); }
  .card--back {
    left: 645px; width: 305px;
    background: radial-gradient(ellipse at 50% 0%, var(--night-top) 0%, var(--night-bottom) 75%);
  }

  .brand-ring {
    position: absolute; width: 92px; height: 92px; border-radius: 50%;
    border: 5px solid var(--brand-red); left: 50%; transform: translateX(-50%);
  }
  .card--front .brand-ring { top: 63px; }
  .card--back .brand-ring { top: 175px; }

  .wordmark {
    position: absolute; left: 0; right: 0; text-align: center;
    font-family: "Exo 2", sans-serif; font-weight: 700;
    font-size: 31px; letter-spacing: 1px; color: var(--brand-red);
  }
  .card--front .wordmark { top: 170px; }
  .card--back .wordmark { top: 282px; }

  .front-arc { position: absolute; left: 0; top: 0; width: 301px; height: 490px; }

  .contact-block {
    position: absolute; left: 0; right: 0; top: 322px; text-align: center;
  }
  .person-name {
    font-family: "Exo 2", sans-serif; font-weight: 600;
    font-size: 22px; letter-spacing: 1.5px; color: var(--brand-red);
    line-height: 26px;
  }
  .person-role {
    font-family: "Exo 2", sans-serif; font-weight: 600;
    font-size: 13px; letter-spacing: .5px; color: var(--text-light);
    margin-top: 3px;
  }
  .divider {
    width: 131px; height: 1px; background: var(--rule);
    margin: 13px auto 14px;
  }
  .contact-line {
    font-family: "Open Sans", sans-serif; font-size: 13px;
    color: var(--text-light); line-height: 20px;
  }
  .contact-line .label { color: var(--brand-red); font-weight: 600; }

  .website {
    position: absolute; left: 0; right: 0; top: 343px; text-align: center;
    font-family: "Open Sans", sans-serif; font-size: 13px; color: var(--brand-red);
  }
</style>
</head>
<body>
<main class="stage">
  <section class="card card--front">
    <svg class="front-arc" viewBox="0 0 301 490" aria-hidden="true">
      <path d="M0 321 Q150 190 301 321 L301 490 L0 490 Z" fill="#000"/>
    </svg>
    <div class="brand-ring"></div>
    <div class="wordmark">FIELD POINT</div>
    <div class="contact-block">
      <div class="person-name">AARON BLAKE</div>
      <div class="person-role">DIRECTOR</div>
      <div class="divider"></div>
      <p class="contact-line"><span class="label">P:</span> 403- 555-0148</p>
      <p class="contact-line"><span class="label">E:</span> hello@fieldpoint.com</p>
    </div>
  </section>

  <section class="card card--back">
    <div class="brand-ring"></div>
    <div class="wordmark">FIELD POINT</div>
    <p class="website">www.fieldpoint.com</p>
  </section>
</main>
</body>
</html>
```